Need a cover for eBook:
Title is: 41 Blunders That Sink Your Indie-Released Volume.
Remarks about the title: I know that is difficult to design a cover with a number. You can add the word TOP (in caps or not) before 41 blunders. It is not mandatory to insert the word TOP. It is up to you if you think you can create a better cover.
Subtitle is: A Newcomer's Manual for Releasing Solo, Arranging Pictures and Words, Planning Pages, Boosting Sign-ups and Moving More Copies
Author: Dennis R. Walbrey
Publisher: Quillmark Press
The book made the presentation of errors that can occur during the production of an ebook. Title must be big, the title should be readable even when the image is reduced in size. No photo please.
I join my projects as an example. Do what you want but I need impact.

Target Market(s)

Book to sell first at Brimfold Reader Shop. Target is authors, men or women, who want to produce ebooks.

Industry/Entity Type

Publishing Company

Font styles to use
Sans Serif

Colors
3176b5
9bcb3c

Requirements
Must have
• High readability when cover is small.
• Here is the definition of the word KILL
• put an end to or cause the failure or defeat of (something).
• "the committee voted to kill the project"
• synonyms: destroy, put an end to, end, extinguish, dash, quash, ruin, wreck, shatter, smash, crush, scotch, thwart; informalput the kibosh on, stymie, scuttle
• "this would kill all hopes of progress"
• veto, defeat, vote down, rule against, reject, throw out, overrule, overturn, put a stop to, quash, squash
• "an opposition attempt to kill the bill"
Nice to have
• I suggested 2 colors but you can you use another one or two. I want cover that sell. There is so bright ideas here. Come on down!
Should not have
• No picture or photo. If a photo or an object had power to the cover, you can insert one. I don't want a photo-collage.

```html
<!DOCTYPE html>
<html lang="en">
<head>
<meta charset="utf-8">
<title>41 Blunders That Sink Your Indie-Released Volume</title>
<link rel="stylesheet" href="https://fonts.googleapis.com/css2?family=Anton&family=Oswald:wght@500;700&display=swap">
<style>
  :root {
    --sky: #3ee3f2;
    --sky-deep: #2fc3d6;
    --royal: #2a7cc2;
    --amber: #eaa23a;
    --white: #ffffff;
    --ink: #1f2a55;
    --ember: #e1643a;
    --shade: rgba(20, 40, 80, 0.55);
    --art-tone: #5aa7b4;
  }
  html, body {
    margin: 0;
    padding: 0;
    overflow: hidden;
    background: #ffffff;
  }
  .cover {
    position: relative;
    width: 753px;
    height: 1200px;
    background: var(--sky);
    overflow: hidden;
    font-family: "Anton", "Oswald", sans-serif;
  }
  .title {
    position: absolute;
    left: 0;
    top: 40px;
    width: 753px;
    margin: 0;
    text-align: center;
    font-weight: 400;
    line-height: 1;
    text-transform: uppercase;
    text-shadow: 3px 4px 0 var(--shade);
  }
  .title .line { display: block; white-space: nowrap; }
  .title .line-number { font-size: 132px; letter-spacing: 2px; }
  .title .line-verb { font-size: 104px; margin-top: 22px; }
  .title .line-object { font-size: 78px; margin-top: 34px; }
  .amber { color: var(--amber); }
  .royal { color: var(--royal); }
  .white { color: var(--white); }
  .art-pages {
    position: absolute;
    left: 100px;
    top: 505px;
    width: 215px;
    height: 110px;
    border-radius: 6px;
    background: var(--sky-deep);
  }
  .art-hunter {
    position: absolute;
    left: 605px;
    top: 520px;
    width: 135px;
    height: 330px;
    border-radius: 6px;
    background: var(--art-tone);
  }
  .subtitle {
    position: absolute;
    left: 88px;
    top: 645px;
    width: 505px;
    margin: 0;
    font-family: "Oswald", sans-serif;
    font-weight: 700;
    font-size: 34px;
    line-height: 1.08;
    letter-spacing: 1px;
    color: var(--white);
    text-transform: uppercase;
    text-shadow: 2px 2px 0 var(--ink);
  }
  .subtitle .payoff {
    display: block;
    margin-top: 14px;
    font-family: "Anton", sans-serif;
    font-weight: 400;
    font-size: 74px;
    line-height: 1.05;
    color: var(--amber);
    letter-spacing: 2px;
    white-space: nowrap;
    text-shadow: 3px 3px 0 var(--shade);
  }
  .credit-band {
    position: absolute;
    left: 0;
    bottom: 0;
    width: 753px;
    height: 163px;
    background: var(--ember);
    text-align: center;
    color: var(--white);
    font-family: "Oswald", sans-serif;
    text-transform: uppercase;
  }
  .author {
    margin: 42px 0 0;
    font-weight: 700;
    font-size: 58px;
    line-height: 1;
    letter-spacing: 2px;
  }
  .publisher {
    margin: 14px 0 0;
    font-weight: 500;
    font-size: 30px;
    letter-spacing: 2px;
  }
</style>
</head>
<body>
  <main class="cover">
    <h1 class="title">
      <span class="line line-number"><span class="amber">41</span> <span class="royal">Blunders</span></span>
      <span class="line line-verb"><span class="white">That</span> <span class="royal">Sink</span> <span class="white">Your</span></span>
      <span class="line line-object"><span class="white">Indie-Released</span> <span class="amber">Volume</span></span>
    </h1>

    <div class="art-pages" role="img" aria-label="Illustration of loose ebook pages and an open book flying through the air"></div>
    <div class="art-hunter" role="img" aria-label="Illustration of a hunter aiming a shotgun at the flying pages"></div>

    <p class="subtitle">
      A Newcomer's Manual for Releasing Solo, Arranging Pictures and Words, Planning Pages, Boosting Sign-ups and
      <span class="payoff">Moving More Copies</span>
    </p>

    <footer class="credit-band">
      <p class="author">Dennis R. Walbrey</p>
      <p class="publisher">Quillmark Press</p>
    </footer>
  </main>
</body>
</html>
```